Custom Wordpress Theme Needed

We need a custom Wordpress theme built with the following features:

1. Flat style design
2. Fully responsive - built for mobile and tablets first; bootstrap or other framework used
3. Flexible - comes with homepage layouts for portfolios, agencies, and magazines
4. Built in 'contact' and 'about us' styling
5. Pre-populated pages and content, including reusable images
6. Multiple slider options

We are completely open to your creativity as far as the overall design style is concerned, but some of our favorites are:
http://themes.plovaro.com/themeselector/?theme=TideBoard
http://www.kelmora.ru/flatmagazine/
http://quarnwellbox.com/wp/velta/intro/
http://theme.dovrask.net/second/

Most unique and in-depth style wins!

Reason: We need more designs!

Reason: Waiting on final submissions and revisions. Thanks!

```html
<!DOCTYPE html>
<html lang="en">
<head>
<meta charset="utf-8">
<title>Ned Carver — Theme Home</title>
<link rel="stylesheet" href="https://fonts.googleapis.com/css2?family=Source+Sans+3:wght@300;400;600&display=swap">
<style>
:root{
  --coral:#f05a5b;
  --band:#ff6566;
  --ink:#333333;
  --muted:#8a8a8a;
  --soft:#9a9a9a;
  --link:#1aa0c8;
  --line:#e3e3e3;
  --panel:#f6f6f6;
  --footer:#2f3233;
  --white:#ffffff;
}
*{box-sizing:border-box;margin:0;padding:0}
html,body{width:1200px;height:2397px;overflow:hidden}
body{position:relative;background:var(--white);font-family:"Source Sans 3",sans-serif;color:var(--ink)}
.abs{position:absolute}
.ph{position:absolute;display:block}

/* header */
.site-header{position:absolute;left:0;top:0;width:1200px;height:115px;background:var(--white)}
.brand{position:absolute;left:85px;top:28px;font-size:48px;font-weight:300;color:var(--ink);line-height:1}
.brand .first{color:var(--coral)}
.main-nav{position:absolute;left:446px;top:52px;display:flex;font-size:18px;line-height:1}
.main-nav a{color:var(--ink);text-decoration:none;padding:0 16px;border-left:1px solid #d6d6d6}
.main-nav a:first-child{border-left:0;padding-left:0;color:var(--coral)}
.main-nav a:last-child{padding-right:0}

/* hero */
.hero{position:absolute;left:0;top:115px;width:1200px;height:494px;background:linear-gradient(90deg,#dfeef6 0%,#eef4ef 35%,#c7dca5 70%,#9fc27a 100%)}
.hero-device{left:687px;top:21px;width:352px;height:420px;border-radius:18px;background:linear-gradient(180deg,#f4f2ee,#dcd9d2)}
.hero-kicker{position:absolute;left:90px;top:124px;font-size:42px;font-weight:300;color:var(--ink)}
.hero-title{position:absolute;left:90px;top:172px;font-size:55px;font-weight:300;color:var(--coral)}
.hero-text{position:absolute;left:92px;top:244px;width:470px;font-size:19px;line-height:25px;color:#555}
.hero-dots{position:absolute;left:97px;top:315px;display:flex;gap:6px}
.hero-dots span{width:14px;height:14px;border-radius:50%;background:#111}
.hero-dots span:first-child{background:#2aa3c9}

/* intro */
.intro-title{position:absolute;left:0;top:650px;width:1200px;text-align:center;font-size:45px;font-weight:300;color:var(--coral)}
.intro-text{position:absolute;left:155px;top:708px;width:890px;text-align:center;font-size:18.5px;line-height:25px;color:var(--soft)}
.divider{position:absolute;left:30px;top:815px;width:1140px;height:16px;background:radial-gradient(ellipse at center top,rgba(0,0,0,.07),rgba(0,0,0,0) 70%)}

.section-title{position:absolute;font-size:32px;font-weight:300;color:var(--ink);line-height:1}

/* news list */
.news-item{position:absolute;left:80px;width:500px;height:84px}
.news-thumb{left:0;top:0;width:128px;height:84px}
.news-body{position:absolute;left:144px;top:-4px;width:350px}
.news-body h3{font-size:17px;font-weight:400;color:#444;line-height:22px}
.news-body p{font-size:13.5px;line-height:20px;color:var(--muted)}
.news-body time{display:block;font-size:14px;color:var(--link);line-height:22px}

/* articles */
.article{position:absolute;top:924px;width:218px}
.article-img{left:0;top:0;width:218px;height:126px}
.article h3{position:absolute;top:140px;font-size:17px;font-weight:400;color:#444;white-space:nowrap}
.article p{position:absolute;top:168px;width:218px;font-size:13.5px;line-height:20.5px;color:var(--muted)}
.article .more{position:absolute;top:282px;left:2px;font-size:13.5px;font-weight:600;color:var(--link);text-decoration:none}

/* popular band */
.popular{position:absolute;left:0;top:1283px;width:1200px;height:406px;background:var(--band)}
.popular .section-title{color:var(--white);left:80px;top:43px}
.pop-card{position:absolute;top:101px;width:252px}
.pop-img{left:0;top:0;width:252px;height:150px}
.pop-card h3{position:absolute;top:162px;left:3px;font-size:17px;font-weight:600;color:var(--white);white-space:nowrap}
.pop-card p{position:absolute;top:188px;left:3px;width:245px;font-size:13.5px;line-height:20.5px;color:#ffe3e3}

/* videos */
.video{position:absolute;width:226px;height:123px}
.video-img{left:0;top:0;width:226px;height:123px}
.play{position:absolute;left:97px;top:45px;width:34px;height:34px}

/* testimonials */
.quote{position:absolute;left:628px;width:494px;background:var(--panel);border:1px solid var(--line)}
.quote svg{position:absolute;left:30px;top:28px}
.quote p{position:absolute;left:90px;top:16px;width:385px;font-size:13.5px;line-height:22px;font-style:italic;color:var(--muted)}
.quote p b{font-style:normal;font-weight:400;color:#444}

/* partners */
.partners{position:absolute;left:0;top:2125px;width:1200px;height:128px;border-top:1px solid var(--line);background:var(--white)}
.badge{position:absolute;top:46px;height:30px;background:#c9c9c9;border-radius:4px}

/* footer */
.site-footer{position:absolute;left:0;top:2253px;width:1200px;height:144px;background:var(--footer)}
.foot-nav{position:absolute;left:94px;top:44px;display:flex;gap:40px;font-size:18px;line-height:1}
.foot-nav a{color:var(--white);text-decoration:none}
.copyright{position:absolute;left:95px;top:80px;font-size:13.5px;color:#8e9192}
.social{position:absolute;left:956px;top:38px;display:flex;gap:10px}
.social span{width:33px;height:33px;border-radius:50%;background:var(--white)}
</style>
</head>
<body>

<header class="site-header">
  <div class="brand"><span class="first">Ned</span> Carver</div>
  <nav class="main-nav">
    <a href="#">HOME</a><a href="#">SERVICES</a><a href="#">ABOUT</a><a href="#">NEWS</a><a href="#">TEAM</a><a href="#">TESTIMONIAL</a><a href="#">CONTACT</a>
  </nav>
</header>

<section class="hero" role="img" aria-label="Blurred sunny beach with palm greenery behind a hand holding a tablet">
  <div class="ph hero-device" role="img" aria-label="Hand holding a tablet showing a classified ads newspaper page"></div>
  <div class="hero-kicker">Mauris vel lacus vitae</div>
  <div class="hero-title">Suspendisse quam leo</div>
  <p class="hero-text">Phasellus felis dolor, scelerisque a, tempus eget, lobortis id, libero. Donec scelerisque leo ac risus.</p>
  <div class="hero-dots"><span></span><span></span><span></span><span></span></div>
</section>

<h1 class="intro-title">Mauris vel lacus vitae felis vestibulum</h1>
<p class="intro-text">Mauris neque metus, malesuada nec, ultricies sit amet, porttitor mattis, enim. In massa libero, interdum nec, interdum vel, blandit sed, nulla. In ullamcorper, est eget tempor cursus, neque mi consectetuer mi</p>
<div class="divider"></div>

<h2 class="section-title" style="left:80px;top:877px">Latest News</h2>

<article class="news-item" style="top:932px">
  <div class="ph news-thumb" role="img" aria-label="Overhead view of a team meeting around a desk" style="background:linear-gradient(135deg,#6f7b7c,#c9cfcf)"></div>
  <div class="news-body"><h3>Mauris vel lacus vitae felis</h3><p>vestibulum volutpat. Etiam est nunc, venenatis in, tristique eu, imperdiet ac, nisl Cum sociis natoque penatibus</p><time>Posted on 28 September 2013</time></div>
</article>
<article class="news-item" style="top:1042px">
  <div class="ph news-thumb" role="img" aria-label="Business people seated in an office lounge" style="background:linear-gradient(135deg,#e8eef2,#8fa2b0)"></div>
  <div class="news-body"><h3>Mauris vel lacus vitae felis</h3><p>vestibulum volutpat. Etiam est nunc, venenatis in, tristique eu, imperdiet ac, nisl Cum sociis natoque penatibus</p><time>Posted on 28 September 2013</time></div>
</article>
<article class="news-item" style="top:1151px">
  <div class="ph news-thumb" role="img" aria-label="Large crowd of people seen from above" style="background:linear-gradient(135deg,#2c2a28,#7d6f66)"></div>
  <div class="news-body"><h3>Mauris vel lacus vitae felis</h3><p>vestibulum volutpat. Etiam est nunc, venenatis in, tristique eu, imperdiet ac, nisl Cum sociis natoque penatibus</p><time>Posted on 28 September 2013</time></div>
</article>

<h2 class="section-title" style="left:657px;top:877px">Latest Articles</h2>

<article class="article" style="left:658px">
  <div class="ph article-img" role="img" aria-label="Smiling businesswoman in glasses" style="background:linear-gradient(135deg,#f3f3f3,#d8b7a0)"></div>
  <h3>Donec scelerisque leo</h3>
  <p>Class aptent taciti sociosqu ad litora torquent per conubia nostra, per inceptos hymenaeos. Proin nulla arcu, nonummy luctus, dictum eget, fermentum et, lorem Nunc porta</p>
  <a class="more" href="#">LEARN MORE</a>
</article>
<article class="article" style="left:903px">
  <div class="ph article-img" role="img" aria-label="Group of business people standing in an office" style="background:linear-gradient(135deg,#e6e9ec,#3c4048)"></div>
  <h3>Selerisque mi tortor</h3>
  <p>Class aptent taciti sociosqu ad litora torquent per conubia nostra, per inceptos hymenaeos. Proin nulla arcu, nonummy luctus, dictum eget, fermentum et, lorem Nunc porta</p>
  <a class="more" href="#">LEARN MORE</a>
</article>

<section class="popular">
  <h2 class="section-title">Most Popular News</h2>
  <article class="pop-card" style="left:80px">
    <div class="ph pop-img" role="img" aria-label="Young woman smiling outdoors" style="background:linear-gradient(135deg,#4d5a33,#c9a083)"></div>
    <h3>Project Tittle</h3><p>Mauris vel lacus vitae felis vestibulum volutpat. Etiam est nunc, venenatis in tristique imperdiet</p>
  </article>
  <article class="pop-card" style="left:337px">
    <div class="ph pop-img" role="img" aria-label="Woman raising her arms against a bright sunset" style="background:linear-gradient(135deg,#fbe9c4,#e39a3a)"></div>
    <h3>Project Tittle</h3><p>Mauris vel lacus vitae felis vestibulum volutpat. Etiam est nunc, venenatis in tristique imperdiet</p>
  </article>
  <article class="pop-card" style="left:598px">
    <div class="ph pop-img" role="img" aria-label="Crowd at an outdoor event" style="background:linear-gradient(135deg,#3a5877,#9a8577)"></div>
    <h3>Project Tittle</h3><p>Mauris vel lacus vitae felis vestibulum volutpat. Etiam est nunc, venenatis in tristique imperdiet</p>
  </article>
  <article class="pop-card" style="left:857px">
    <div class="ph pop-img" role="img" aria-label="Senior couple cycling in a park" style="background:linear-gradient(135deg,#86a96a,#7fb6d4)"></div>
    <h3>Project Tittle</h3><p>Mauris vel lacus vitae felis vestibulum volutpat. Etiam est nunc, venenatis in tristique imperdiet</p>
  </article>
</section>

<h2 class="section-title" style="left:82px;top:1735px">Popular Videos</h2>

<div class="video" style="left:85px;top:1787px">
  <div class="ph video-img" role="img" aria-label="Man in a red shirt at an office desk" style="background:linear-gradient(135deg,#b9b6ad,#c94a3b)"></div>
  <svg class="play" viewBox="0 0 34 34"><circle cx="17" cy="17" r="17" fill="#222"/><path d="M13 10l11 7-11 7z" fill="#fff"/></svg>
</div>
<div class="video" style="left:328px;top:1787px">
  <div class="ph video-img" role="img" aria-label="Senior woman exercising with dumbbells" style="background:linear-gradient(135deg,#8a5a2c,#d9c3a4)"></div>
  <svg class="play" viewBox="0 0 34 34"><circle cx="17" cy="17" r="17" fill="#222"/><path d="M13 10l11 7-11 7z" fill="#fff"/></svg>
</div>
<div class="video" style="left:85px;top:1927px">
  <div class="ph video-img" role="img" aria-label="Two colleagues talking in an office" style="background:linear-gradient(135deg,#5e7a8c,#2a2624)"></div>
  <svg class="play" viewBox="0 0 34 34"><circle cx="17" cy="17" r="17" fill="#222"/><path d="M13 10l11 7-11 7z" fill="#fff"/></svg>
</div>
<div class="video" style="left:328px;top:1927px">
  <div class="ph video-img" role="img" aria-label="Businesswoman in a library" style="background:linear-gradient(135deg,#7a5a40,#e7e2dc)"></div>
  <svg class="play" viewBox="0 0 34 34"><circle cx="17" cy="17" r="17" fill="#222"/><path d="M13 10l11 7-11 7z" fill="#fff"/></svg>
</div>

<h2 class="section-title" style="left:628px;top:1735px">Testimonials</h2>

<blockquote class="quote" style="top:1777px;height:112px">
  <svg width="42" height="34" viewBox="0 0 42 34"><path d="M2 2h12l6 30H8z M22 2h12l6 30H28z" fill="#2aa3c9"/></svg>
  <p>Phasellus felis dolor, scelerisque a, tempus eget, lobortis id, libero Donec scelerisque leo ac risus Praesent sit amet est In dictum dolor eu dictum porttitor - <b>By Author name</b></p>
</blockquote>
<blockquote class="quote" style="top:1916px;height:125px">
  <svg width="42" height="34" viewBox="0 0 42 34"><path d="M2 2h12l6 30H8z M22 2h12l6 30H28z" fill="#2aa3c9"/></svg>
  <p>Mauris neque metus, malesuada nec, ultricies sit amet, porttitor mattis, enim. In massa libero, interdum nec, interdum vel, blandit sed, nulla. In ullamcorper, est eget tempor cursus neque mi consectetuer mi, a ultricies massa est sed - <b>By Author name</b></p>
</blockquote>

<section class="partners" aria-label="Partner accreditations">
  <div class="badge" style="left:165px;width:48px"></div>
  <div class="badge" style="left:251px;width:52px"></div>
  <div class="badge" style="left:342px;width:48px"></div>
  <div class="badge" style="left:438px;width:104px"></div>
  <div class="badge" style="left:580px;width:58px"></div>
  <div class="badge" style="left:682px;width:60px;border-radius:50%"></div>
  <div class="badge" style="left:774px;width:80px"></div>
  <div class="badge" style="left:887px;width:72px"></div>
  <div class="badge" style="left:992px;width:44px;border-radius:50%"></div>
</section>

<footer class="site-footer">
  <nav class="foot-nav">
    <a href="#">HOME</a><a href="#">FEATURES</a><a href="#">ABOUT</a><a href="#">BLOG</a><a href="#">SIGN IN</a><a href="#">LOGIN</a>
  </nav>
  <p class="copyright">© 2013 Company Name.&nbsp; All right reserved.&nbsp; Term of Use</p>
  <div class="social" aria-label="Social links"><span></span><span></span><span></span><span></span></div>
</footer>

</body>
</html>
```